Book Cover for Memoir: Sexual Assault and Traumatic Stress

I need a cover design for a memoir that is a victim's story of a sexual assault. I will need a print-on-demand cover, an eBook cover, and a 3D thumbnail image. The thumbnail and eBook cover will be used immediately, and the POD cover will be used in a few months with the full manuscript is ready. Therefore, I need an artist who is willing to make small adjustments if needed once the page count is set.

I have a image I have purchased that should give you an idea of the desired direction, but you can feel free to use your own images. I have attached some examples of book covers I like. I attached a color palette for fonts.

Overall Look: Fonts should be feminine and thin, but large to stand out. Look should be simple and elegant, and display and overall depressing feeling. There should be enough detail though to make it look professionally put together. Not TOO minimalistic.

I have also attached the Print Harbor templates if you choose to use those. If not, ensure there is an open place for the barcode on the bottom right.

Requirements
Must have
• Title: Beneath Quiet Rain
Subtitle: One Woman's Account of Fear, Guilt & Silence
Author: Dana Ruth Whitford
Audience: Mostly women 18-30
Quote (for the back): "I always thought I'd know how I'd react if I ever was raped. I was wrong. I've been wrong a lot lately."
Summary (back cover): When twenty-seven-year-old Dana Whitford wakes up with a gut-wrenching feeling, she has little memory of the horrifying events that occurred the night before. Days earlier, Dana was a spirited single mom who had abandoned her hometown to raise her daughter in the city and pursue her dreams. In the short months since Dana’s move to Seattle, she became the adored lover of a charismatic lawyer, started a new business, and finally felt life was going her way. So what happened to cause her to break?

In a gripping and heartbreaking narrative, Dana tells the true story of how her life unraveled from the traumatic events that took place that night and why what seems obvious to everyone else is impossible for Dana to believe. Beneath Quiet Rain is a chilling exploration of memory through trauma, trust in humanity, and a captivating story of strength and survival that appeals to the heart of fathers and mothers, sons and daughters, and men and women alike.
Nice to have
• BACK COVER: I'd like to have a photo on the back. This should depict the happy life of the main character before the sexual assault, and should be with her daughter. Or should be a nature scene that starts at the corner and blends into the rest of the cover. I have attached a possible image or you can use something you like.

```html
<!DOCTYPE html>
<html lang="en">
<head>
<meta charset="UTF-8">
<title>Beneath Quiet Rain – Book Cover</title>
<link rel="stylesheet" href="https://fonts.googleapis.com/css2?family=Montserrat:ital,wght@0,300;0,400;0,600;0,700;0,800;1,500&display=swap">
<style>
  :root {
    --stage: #ececec;
    --sun: #f2c631;
    --sun-soft: #f6dc7a;
    --sea: #3f9fd6;
    --sea-deep: #2d7fc0;
    --back-top: #efeee6;
    --back-mid: #f1efe2;
    --back-bottom: #cfe3ee;
    --ink: #141414;
    --white: #ffffff;
    --placeholder: #e3d6c6;
  }
  * { box-sizing: border-box; margin: 0; padding: 0; }
  html, body {
    width: 1200px; height: 800px; overflow: hidden;
    background: var(--stage);
    font-family: "Montserrat", Arial, sans-serif;
  }
  .cover-wrap {
    position: absolute; left: 120px; top: 55px;
    width: 960px; height: 690px;
    display: flex;
    box-shadow: 0 10px 30px rgba(0,0,0,.18);
  }

  /* Back cover */
  .back-cover {
    width: 460px; height: 100%;
    position: relative;
    padding: 30px 34px 0;
    background: linear-gradient(180deg, var(--back-top) 0%, var(--back-mid) 55%, var(--back-bottom) 100%);
    color: var(--ink);
  }
  .back-author {
    text-align: right; font-weight: 700; font-size: 13px; letter-spacing: .5px;
  }
  .back-title {
    font-weight: 800; font-size: 32px; letter-spacing: -.5px; line-height: 1.05;
    margin-top: 4px; white-space: nowrap;
  }
  .back-subtitle {
    font-weight: 800; font-size: 12.5px; letter-spacing: .2px; margin-top: 3px;
    white-space: nowrap;
  }
  .back-blurb {
    margin-top: 14px;
    font-weight: 600; font-size: 12.2px; line-height: 1.48;
    text-align: justify; text-align-last: center;
  }
  .back-blurb p + p { margin-top: 2px; }
  .back-quote {
    margin-top: 12px;
    font-style: italic; font-weight: 500; font-size: 12.2px; line-height: 1.45;
    text-align: center;
  }
  .back-marks {
    position: absolute; left: 60px; right: 60px; bottom: 34px;
    display: flex; justify-content: space-between;
  }
  .mark-box {
    width: 140px; height: 64px; background: var(--placeholder);
    display: flex; align-items: center; justify-content: center;
    font-weight: 700; font-size: 12px;
  }

  /* Spine */
  .spine {
    width: 40px; height: 100%;
    background: linear-gradient(180deg, var(--sun) 0%, var(--sun-soft) 45%, var(--sea) 100%);
    display: flex; align-items: center; justify-content: space-between;
    writing-mode: vertical-rl;
    padding: 18px 0;
  }
  .spine-title { font-weight: 800; font-size: 22px; color: var(--ink); letter-spacing: 1px; }
  .spine-author { font-weight: 600; font-size: 11px; color: var(--ink); letter-spacing: 1px; }

  /* Front cover */
  .front-cover {
    width: 460px; height: 100%; position: relative; overflow: hidden;
    color: var(--white);
  }
  .front-photo {
    position: absolute; inset: 0;
    background:
      radial-gradient(ellipse at 45% 40%, rgba(120,90,60,.35) 0%, rgba(120,90,60,0) 55%),
      linear-gradient(180deg, var(--sun) 0%, #eec84a 30%, #b9c98a 55%, var(--sea) 78%, var(--sea-deep) 100%);
  }
  .front-circle { position: absolute; inset: 0; }
  .front-title {
    position: absolute; left: 50px; right: 20px; top: 110px;
    font-weight: 300; font-size: 70px; line-height: 1; letter-spacing: -1px;
    text-transform: uppercase; white-space: nowrap;
  }
  .front-subtitle {
    position: absolute; left: 0; right: 0; top: 540px;
    text-align: center; font-weight: 700; font-size: 17px; line-height: 1.25;
    text-transform: uppercase; letter-spacing: .3px;
  }
  .front-author {
    position: absolute; left: 0; right: 0; bottom: 28px;
    text-align: center; font-weight: 700; font-size: 13px; letter-spacing: 1px;
    text-transform: uppercase;
  }
</style>
</head>
<body>
  <main class="cover-wrap">
    <section class="back-cover">
      <p class="back-author">DANA RUTH WHITFORD</p>
      <h2 class="back-title">BENEATH QUIET RAIN</h2>
      <p class="back-subtitle">ONE WOMAN'S ACCOUNT OF FEAR, GUILT &amp; SILENCE</p>
      <div class="back-blurb">
        <p>When twenty-seven-year-old Dana Whitford wakes up with a gut-wrenching feeling, she has little memory of the horrifying events that occurred the night before. Days earlier, Dana was a spirited single mom who had abandoned her hometown to raise her daughter in the city and pursue her dreams. In the short months since Dana’s move to Seattle, she became the adored lover of a charismatic lawyer, started a new business, and finally felt life was going her way. So what happened to cause her to break?</p>
        <p>In a gripping and heartbreaking narrative, Dana tells the true story of how her life unraveled from the traumatic events that took place that night and why what seems obvious to everyone else is impossible for Dana to believe. Beneath Quiet Rain is a chilling exploration of memory through trauma, trust in humanity, and a captivating story of strength and survival that appeals to the heart of fathers and mothers, sons and daughters, and men and women alike.</p>
      </div>
      <blockquote class="back-quote">“I always thought I'd know how I'd react if I ever was raped. I was wrong. I've been wrong a lot lately.”</blockquote>
      <div class="back-marks">
        <div class="mark-box">LOGO</div>
        <div class="mark-box">ISBN</div>
      </div>
    </section>

    <aside class="spine">
      <span class="spine-title">BENEATH QUIET RAIN</span>
      <span class="spine-author">DANA RUTH WHITFORD</span>
    </aside>

    <section class="front-cover">
      <div class="front-photo" role="img" aria-label="Photo of a young woman sitting on a bed, hugging her knees with her head bowed, in warm yellow and cool blue light"></div>
      <svg class="front-circle" width="460" height="690" viewBox="0 0 460 690" aria-hidden="true">
        <circle cx="235" cy="300" r="215" fill="#ffffff" fill-opacity=".12"/>
      </svg>
      <h1 class="front-title">Beneath<br>Quiet<br>Rain</h1>
      <p class="front-subtitle">One Woman's Account of<br>Fear, Guilt &amp; Silence</p>
      <p class="front-author">Dana Ruth Whitford</p>
    </section>
  </main>
</body>
</html>
```